Start up in business consultancy needs a business card

We need the business card's layout (we have already the logo). Our business is concerned on consultancy services delivered to companies on the matter of sustainability. Business card should be enough essentials and professional style.

Side A with the following info:
logo + a space for the claim (still to identify) + website of the company

Side B with the following info:
Name of business card holder + title of the business card holder + address of the company + space for mobile number, phone number, fax number + e-mail of business card holder + graphic details around.

Target Market(s)

Business of any sector

Industry/Entity Type

Business Service

Contact Information for Business Card

Name of the company:
Pianoverde srl
Società Benefit

Address of the company:
Via Lucerna, 7
21047 - Saronno (VA)

Website:
www.pianoverde.it

Name of the BC' holder:
Luca Ferentino

Title:
Co-fondatore

Email:
luca@pianoverde.it

Mobile:
+39 348 915 2074
Phone:
+39 348 915 2074
Fax:
+39 348 915 2074

Font styles to use
Other font styles liked:
• new gothic

```html
<!DOCTYPE html>
<html lang="it">
<head>
<meta charset="utf-8">
<title>Pianoverde – biglietto da visita</title>
<link rel="stylesheet" href="https://fonts.googleapis.com/css2?family=Questrial&family=Open+Sans:wght@400;600&family=Open+Sans+Condensed:wght@300&display=swap">
<style>
  :root {
    --backdrop: #7d7d7d;
    --card-white: #ffffff;
    --brand-blue: #0a67b0;
    --brand-blue-deep: #0058a0;
    --ink-grey: #555a5f;
    --ink-dark: #333639;
    --on-blue: #ffffff;
  }
  * { box-sizing: border-box; margin: 0; padding: 0; }
  html, body { width: 1200px; height: 900px; overflow: hidden; }
  body {
    background: var(--backdrop);
    display: flex;
    align-items: center;
    justify-content: center;
    gap: 60px;
  }
  .card {
    position: relative;
    width: 520px;
    height: 325px;
    border-radius: 26px;
    overflow: hidden;
  }

  /* Contact side */
  .card--contact { background: var(--card-white); color: var(--ink-grey); }
  .contact__brand {
    position: absolute; left: 44px; top: 34px;
    font-family: "Questrial", sans-serif;
    font-size: 44px; letter-spacing: -1px;
    color: var(--brand-blue);
  }
  .contact__holder { position: absolute; left: 44px; top: 104px; }
  .holder__name {
    font-family: "Open Sans", sans-serif; font-weight: 600;
    font-size: 21px; text-transform: uppercase; color: var(--ink-grey);
  }
  .holder__name .surname { color: var(--brand-blue); }
  .holder__title {
    font-family: "Open Sans", sans-serif; font-weight: 600;
    font-size: 12px; text-transform: uppercase; letter-spacing: .5px;
    color: var(--ink-grey); margin-top: 2px;
  }
  .contact__rule {
    position: absolute; left: 44px; right: 0; top: 170px;
    height: 2px; background: var(--brand-blue);
  }
  .contact__address {
    position: absolute; right: 36px; top: 118px; text-align: left;
    font-family: "Questrial", sans-serif; font-size: 13px;
    text-transform: uppercase; letter-spacing: .6px; line-height: 1.5;
    color: var(--ink-grey);
  }
  .contact__list { position: absolute; list-style: none; }
  .contact__list--phones { left: 44px; top: 192px; }
  .contact__list--web { right: 36px; top: 196px; }
  .contact__list li {
    display: flex; align-items: center; gap: 12px;
    font-family: "Open Sans Condensed", "Open Sans", sans-serif; font-weight: 300;
    font-size: 15px; color: var(--ink-dark); height: 25px;
  }
  .contact__list svg { width: 14px; height: 14px; flex: none; }
  .icon { fill: none; stroke: var(--brand-blue); stroke-width: 1.5; stroke-linecap: round; stroke-linejoin: round; }

  /* Brand side */
  .card--brand {
    background: linear-gradient(135deg, var(--brand-blue) 0%, var(--brand-blue-deep) 100%);
    color: var(--on-blue);
  }
  .brand__lockup {
    position: absolute; left: 60px; top: 108px;
    display: flex; align-items: center; gap: 20px;
  }
  .brand__dot {
    width: 70px; height: 70px; border-radius: 50%;
    border: 4px solid var(--on-blue);
  }
  .brand__name {
    font-family: "Questrial", sans-serif; font-size: 56px;
    letter-spacing: -1px; color: var(--on-blue);
  }
  .brand__url {
    position: absolute; right: 40px; bottom: 30px;
    font-family: "Open Sans", sans-serif; font-size: 15px;
    letter-spacing: 1px; color: var(--on-blue);
  }
</style>
</head>
<body>

<section class="card card--contact" aria-label="Fronte contatti">
  <div class="contact__brand">pianoverde</div>

  <div class="contact__holder">
    <p class="holder__name">Luca <span class="surname">Ferentino</span></p>
    <p class="holder__title">Co-founder</p>
  </div>

  <p class="contact__address">Via Lucerna, 2<br>21047-Saronno (VA)</p>

  <div class="contact__rule"></div>

  <ul class="contact__list contact__list--phones">
    <li>
      <svg viewBox="0 0 14 14" aria-hidden="true"><rect class="icon" x="3.5" y="1" width="7" height="12" rx="1.2"/></svg>
      +39 348 915 2074
    </li>
    <li>
      <svg viewBox="0 0 14 14" aria-hidden="true"><path class="icon" d="M3 1.5 5 4 4 5.5c1 2 2.5 3.5 4.5 4.5L10 9l2.5 2-1 1.5C6 12 2 8 1.5 2.5z"/></svg>
      +39 348 915 2074
    </li>
    <li>
      <svg viewBox="0 0 14 14" aria-hidden="true"><rect class="icon" x="1.5" y="5" width="11" height="7" rx="1"/><rect class="icon" x="4" y="1.5" width="6" height="3.5"/><path class="icon" d="M4 8.5h6"/></svg>
      +39 348 915 2074
    </li>
  </ul>

  <ul class="contact__list contact__list--web">
    <li>
      <svg viewBox="0 0 14 14" aria-hidden="true"><rect class="icon" x="1.5" y="3" width="11" height="8"/><path class="icon" d="M1.5 3 7 7.5 12.5 3"/></svg>
      luca@pianoverde.it
    </li>
    <li>
      <svg viewBox="0 0 14 14" aria-hidden="true"><circle class="icon" cx="7" cy="7" r="5.5"/><ellipse class="icon" cx="7" cy="7" rx="2.4" ry="5.5"/><path class="icon" d="M1.5 7h11"/></svg>
      www.pianoverde.it
    </li>
  </ul>
</section>

<section class="card card--brand" aria-label="Retro marchio">
  <div class="brand__lockup">
    <span class="brand__dot" aria-hidden="true"></span>
    <span class="brand__name">pianoverde</span>
  </div>
  <p class="brand__url">www.pianoverde.it</p>
</section>

</body>
</html>
```